依頼概要
■ 概要・特徴

メヒカリの唐揚げは居酒屋さんのメニューですが、コロナで飲食業に業務用1kgの卸業が厳しいので、ネットで小売り200gのスーパー販売や、ギフトとして販売をしたいです。
小売りパッケージはレシピやインパクトのあるものがよいかと思います。

■ 依頼詳細

メヒカリの唐揚粉付 油であげるだけで簡単調理!
宮崎県北浦穫れの鮮度抜群のメヒカリを、1回きりの瞬間冷凍で小売りやギフトのパッケージシール 油であげるだけで簡単調理!様々な料理のアレンジできます。コロナで外食ができないので酒のおつまみや、ご家庭でプチぜいたくを
レシピを載せたらいいかもしれません。

■ ポーズ数

1ポーズ

■ 希望する色

茶系、黄・オレンジ系

■ 納品ファイル

■ 補足説明

よくわからいですが、Aiだと私がみれないので、PDFが良いです
透明の袋にシールを張るか、タグ付きのデザインで袋ではございません。
■ 選んだ理由

居酒屋さんメニューなので、自宅で居酒屋さん気分を味わっていただけるようなデザインでした。

■ 提案者全員のお礼・コメント

他に食品のデザインを募集しますのでよろしくお願い致します。

```html
<!DOCTYPE html>
<html lang="ja">
<head>
<meta charset="utf-8">
<title>メヒカリの唐揚粉付</title>
<link rel="stylesheet" href="https://fonts.googleapis.com/css2?family=Noto+Serif+JP:wght@700;900&display=swap">
<style>
  :root {
    --paper: #ffffff;
    --ink: #111111;
    --brown: #6a1c14;
    --brown-deep: #4e120c;
    --orange: #e8931f;
    --amber: #f2b24a;
    --accent-red: #7a1f16;
    --cream: #f6e6c8;
  }
  * { margin: 0; padding: 0; box-sizing: border-box; }
  html, body { width: 800px; height: 1200px; overflow: hidden; background: var(--paper); }
  .label {
    position: relative;
    width: 800px;
    height: 1200px;
    background: var(--paper);
    font-family: "Noto Serif JP", serif;
    overflow: hidden;
  }
  .pattern {
    position: absolute;
    left: 0;
    width: 800px;
  }
  .pattern-top { top: 0; height: 360px; }
  .pattern-bottom { bottom: 0; height: 420px; }
  .product-name {
    position: absolute;
    left: 0;
    width: 800px;
    top: 330px;
    text-align: center;
    font-size: 124px;
    font-weight: 900;
    color: var(--ink);
    letter-spacing: 4px;
    line-height: 1;
  }
  .product-sub {
    position: absolute;
    top: 540px;
    left: 370px;
    color: var(--ink);
    font-weight: 900;
    line-height: 1;
    white-space: nowrap;
  }
  .product-sub .particle { font-size: 44px; margin-right: 18px; vertical-align: 14px; }
  .product-sub .kind { font-size: 60px; letter-spacing: 2px; }
  .tagline {
    position: absolute;
    top: 690px;
    left: 190px;
    width: 400px;
    text-align: center;
    color: var(--accent-red);
    font-size: 38px;
    font-weight: 700;
    line-height: 1.9;
    letter-spacing: 1px;
  }
  .net-weight {
    position: absolute;
    right: 22px;
    bottom: 28px;
    color: var(--cream);
    font-size: 42px;
    font-weight: 700;
    line-height: 1;
  }
</style>
</head>
<body>
<main class="label">
  <svg class="pattern pattern-top" viewBox="0 0 800 360" role="img" aria-label="茶色とオレンジの波しぶき模様の装飾">
    <defs>
      <radialGradient id="topGlow" cx="0.65" cy="0.35" r="0.8">
        <stop offset="0" stop-color="#8a3418"/>
        <stop offset="0.55" stop-color="#6a1c14"/>
        <stop offset="1" stop-color="#4e120c"/>
      </radialGradient>
    </defs>
    <path d="M0 0 H800 V300 C720 330 640 320 560 300 C470 278 380 300 290 290 C200 280 140 250 80 235 C50 228 20 232 0 240 Z" fill="url(#topGlow)"/>
    <path d="M0 240 C20 232 50 228 80 235 C140 250 200 280 290 290 C380 300 470 278 560 300 C640 320 720 330 800 300" fill="none" stroke="#e8931f" stroke-width="6"/>
  </svg>

  <h1 class="product-name">メヒカリ</h1>
  <p class="product-sub"><span class="particle">の</span><span class="kind">唐揚粉付</span></p>
  <p class="tagline">油であげるだけで<br>簡単調理！</p>

  <svg class="pattern pattern-bottom" viewBox="0 0 800 420" role="img" aria-label="茶色とオレンジの波しぶき模様の装飾">
    <defs>
      <radialGradient id="bottomGlow" cx="0.35" cy="0.6" r="0.85">
        <stop offset="0" stop-color="#8a3418"/>
        <stop offset="0.55" stop-color="#6a1c14"/>
        <stop offset="1" stop-color="#4e120c"/>
      </radialGradient>
    </defs>
    <path d="M0 90 C60 60 120 40 190 55 C260 70 300 110 380 105 C470 98 540 60 630 55 C700 52 760 70 800 40 V420 H0 Z" fill="url(#bottomGlow)"/>
    <path d="M0 90 C60 60 120 40 190 55 C260 70 300 110 380 105 C470 98 540 60 630 55 C700 52 760 70 800 40" fill="none" stroke="#e8931f" stroke-width="6"/>
  </svg>

  <p class="net-weight">200g</p>
</main>
</body>
</html>
```